Zielgruppe
Friseurin für Damen und Herren
Aufgabenstellung
https://lumiraschnitt.de
Bitte erstelle mir anhand der Daten von der Website einen angepassten Entwurf mit Neueröffnung und geben keine Preise an sondern die kunden sollen sich direkt eingeladen führen um persönlich vor Ort vorbei zuschauen.

```html
<!DOCTYPE html>
<html lang="de">
<head>
<meta charset="utf-8">
<title>Lumira Hair &amp; Beautylounge – Neueröffnung</title>
<link rel="stylesheet" href="https://fonts.googleapis.com/css2?family=Montserrat:ital,wght@0,400;0,600;0,700;1,400&display=swap">
<style>
  :root {
    --rose: #e6c6b8;
    --sage: #6b7a5b;
    --ink: #1c1c1c;
    --logo-ink: #2a3230;
    --white: #ffffff;
    --blush-text: #ebc7b5;
  }
  * { margin: 0; padding: 0; box-sizing: border-box; }
  html, body { width: 1200px; height: 851px; overflow: hidden; }
  body { font-family: "Montserrat", sans-serif; background: var(--sage); }
  .card { position: relative; width: 1200px; height: 851px; overflow: hidden; background: var(--sage); }
  .backdrop { position: absolute; inset: 0; }
  .frame {
    position: absolute; left: 46px; top: 60px; width: 1116px; height: 744px;
    border: 2px solid var(--white);
  }
  .logo-box {
    position: absolute; left: 412px; top: 0; width: 376px; height: 196px;
    background: var(--white); display: flex; flex-direction: column;
    align-items: center; justify-content: center; padding-top: 4px;
    color: var(--logo-ink); font-weight: 400;
  }
  .logo-name { font-size: 66px; letter-spacing: 0; line-height: 1; }
  .logo-sub { font-size: 29px; letter-spacing: -1px; margin-top: 16px; white-space: nowrap; }
  .intro {
    position: absolute; left: 43px; width: 720px; top: 280px;
    text-align: center; color: var(--ink); font-size: 20.5px; line-height: 31.5px;
  }
  .intro p { margin-bottom: 31.5px; }
  .intro strong { font-weight: 700; }
  .contact {
    position: absolute; left: 816px; width: 300px; top: 238px;
    text-align: center; color: var(--white); font-size: 21px; line-height: 31.5px;
  }
  .contact-title { color: var(--blush-text); font-weight: 700; letter-spacing: 0.5px; margin-bottom: 31px; }
  .contact-details { margin-bottom: 31px; }
  .contact-details a { color: inherit; text-decoration: none; }
  .welcome { color: var(--blush-text); font-style: italic; text-transform: uppercase; letter-spacing: 0.5px; }
</style>
</head>
<body>
<main class="card">
  <svg class="backdrop" width="1200" height="851" viewBox="0 0 1200 851" aria-hidden="true">
    <rect width="1200" height="851" fill="var(--sage)"/>
    <circle cx="220" cy="516" r="604" fill="var(--rose)"/>
  </svg>
  <div class="frame"></div>

  <header class="logo-box">
    <div class="logo-name">LUMIRA</div>
    <div class="logo-sub">HAIR &amp; BEAUTYLOUNGE</div>
  </header>

  <section class="intro">
    <p><strong>Neueröffnung! Erlebe unseren modernen Salon,<br>in dem sich alles um dich und deinen Look dreht.</strong></p>
    <p>Wir nehmen uns Zeit für dich, beraten dich persönlich<br>und verbinden handwerkliche Präzision mit viel Leidenschaft.</p>
    <p><strong>Unsere Leistungen für dich:</strong><br>
      Frische Haarschnitte für Damen, Herren &amp; Kinder,<br>
      strahlende Colorationen, Glossing &amp; Balayage,<br>
      Extensions &amp; Haarverdichtung, Styling für besondere Anlässe,<br>
      sowie Pflege-Treatments für gesundes, glänzendes Haar.</p>
    <p>Komm zur Eröffnung vorbei oder vereinbare deinen Termin!</p>
  </section>

  <aside class="contact">
    <div class="contact-title">LUMIRA HAIR &amp;<br>BEAUTYLOUNGE</div>
    <div class="contact-details">
      Birkenweg 7<br>
      86999 Lindenfeld<br>
      Tel.: 08231 45 27 18 0<br>
      Mobil: 0151 234 567 89<br>
      Web: <a href="https://lumiraschnitt.de">lumiraschnitt.de</a>
    </div>
    <div class="welcome">Wir freuen uns,<br>dich zur Neueröffnung<br>persönlich<br>in der Lumira Hair &amp;<br>Beautylounge zu<br>begrüßen.</div>
  </aside>
</main>
</body>
</html>
```